Newsletter Design Project

I need a new design for a monthly newsletter that I do for Academy of Lifelong Pursuits Brisbane. I have been doing the same thing since 2009. We are based in Brisbane and we run classes for semi retired and retired people. I write about social activities, class activities, vacancies etc. I take photos and include them we hhave a logo that I always use. and would just like the newsletter to look different and fresh. The logo is Blue

```html
<!DOCTYPE html>
<html lang="en">
<head>
<meta charset="utf-8">
<title>E Newsletter – May 2013</title>
<link href="https://fonts.googleapis.com/css2?family=Jost:wght@400;500;600;700&display=swap" rel="stylesheet">
<style>
  :root {
    --navy: #0c0c5c;
    --royal: #3535ee;
    --bright: #2a2ae0;
    --ink: #0a0a40;
    --white: #ffffff;
    --photo-warm: #c9a58f;
    --photo-cool: #b9b6c4;
  }
  * { box-sizing: border-box; margin: 0; padding: 0; }
  html, body { width: 848px; height: 1200px; overflow: hidden; background: var(--navy); }
  body { font-family: "Jost", Arial, sans-serif; color: var(--white); position: relative; }

  .masthead { position: absolute; left: 0; top: 0; width: 848px; height: 312px; }
  .masthead svg { position: absolute; left: 0; top: 0; }
  .brand {
    position: absolute; left: 174px; top: 58px; width: 500px; text-align: center;
    font-weight: 700; color: var(--royal);
  }
  .brand-mark { display: inline-block; width: 26px; height: 26px; background: var(--royal); }
  .brand-name { font-size: 21px; line-height: 1.2; margin-top: 14px; white-space: nowrap; }

  .issue-title { position: absolute; left: 0; width: 848px; text-align: center; top: 196px; font-size: 52px; font-weight: 700; line-height: 1; }
  .issue-date { position: absolute; left: 0; width: 848px; text-align: center; top: 250px; font-size: 31px; font-weight: 500; color: var(--ink); line-height: 1; }

  .section { position: absolute; left: 100px; width: 628px; }
  .section h2 { font-size: 32px; font-weight: 600; line-height: 1; position: relative; }
  .section h3 { font-size: 19px; font-weight: 600; line-height: 1.2; position: relative; white-space: nowrap; }
  .section h2::before, .section h3::before { content: "\2726"; position: absolute; left: -24px; font-size: 13px; top: 50%; transform: translateY(-50%); }
  .section p { font-size: 15.6px; line-height: 1.33; margin-left: -36px; }

  .term { top: 320px; }
  .president { top: 390px; }
  .bus { top: 572px; }
  .rule { position: absolute; left: 0; top: 684px; width: 848px; height: 1px; background: #2a2a80; }
  .district { top: 694px; }

  .district-card { position: absolute; left: 64px; width: 751px; }
  .district-card .label { background: var(--bright); font-size: 19px; font-weight: 600; height: 25px; line-height: 25px; padding-left: 4px; }
  .district-card .photo { position: absolute; left: 0; top: 32px; width: 150px; background: var(--white); padding: 4px; }
  .district-card .photo div { width: 100%; height: 100%; }
  .district-card .quote { position: absolute; left: 157px; top: 32px; right: 0; background: var(--white); color: var(--ink); font-size: 14.8px; line-height: 1.4; padding: 8px 12px; }

  .wynnum { top: 741px; }
  .wynnum .photo, .wynnum .quote { height: 130px; }
  .wynnum .photo div { background: linear-gradient(160deg, var(--photo-cool), #8f8a96 60%, #d8d2d0); }

  .logan { top: 950px; }
  .logan .photo, .logan .quote { height: 132px; }
  .logan .photo div { background: linear-gradient(150deg, #6a4a3a, var(--photo-warm) 55%, #a57a64); }

  .footer-bands { position: absolute; left: 0; top: 1158px; width: 848px; }
  .footer-bands .a { height: 6px; background: var(--royal); }
  .footer-bands .b { height: 4px; background: var(--navy); }
  .footer-bands .c { height: 18px; background: #1e1eb0; }
</style>
</head>
<body>
  <header class="masthead">
    <svg width="848" height="312" viewBox="0 0 848 312" aria-hidden="true">
      <rect width="848" height="312" fill="#3535ee"/>
      <path d="M0 0 H848 V10 C760 110 520 170 300 172 C180 172 80 155 0 130 Z" fill="#ffffff"/>
      <path d="M0 100 C120 150 320 170 470 160 C640 148 780 90 848 10 V40 C770 120 620 180 460 186 C300 190 120 170 0 130 Z" fill="#0c0c5c"/>
      <path d="M780 0 C815 20 835 40 848 60 V0 Z" fill="#3535ee"/>
      <path d="M0 128 C140 172 330 190 470 186 C630 180 770 120 848 40 V56 C770 136 630 196 470 200 C310 204 130 182 0 145 Z" fill="#ffffff" opacity="0.35"/>
    </svg>
    <div class="brand">
      <span class="brand-mark"></span>
      <div class="brand-name">Academy of Lifelong Pursuits Brisbane</div>
    </div>
    <h1 class="issue-title">E Newsletter</h1>
    <div class="issue-date">May 2013</div>
  </header>

  <section class="section term">
    <h2>Term 2:</h2>
    <p>Did you realise that we are nearly half way through this term? 2013 seems to be racing</p>
  </section>

  <section class="section president">
    <h2>Message from the President:</h2>
    <p>Alan says “I have access to a large group of book publishers—<br>
    Harbourline Books, Westmark, Riverbend Press, Fernhill Press and many more— who would like older people to review their latest books. These include fiction, non fiction and poetry.”<br>
    If you would like to write a book review (and keep the new publications as your own) please contact the President, Alan Pritchard at apritchard@lifelongmail.net</p>
  </section>

  <section class="section bus">
    <h3>Bus Review from the Riverside City Council. The link is as follows:</h3>
    <p style="margin-top:8px">http//www.riversidecity.example/traffic-transport/public-transport/buses/bus-network-review/index.htm<br>
    This will allow you to assess if you need to object to any of the changes.</p>
  </section>

  <div class="rule"></div>

  <section class="section district">
    <h3 style="font-size:25px">District information:</h3>
  </section>

  <article class="district-card wynnum">
    <div class="label">Wynnum: from Margaret Hale</div>
    <div class="photo"><div role="img" aria-label="Photo of a member wearing a birthday tiara"></div></div>
    <div class="quote">“Our Wynnum Calligraphy Group recently celebrated the 80th birthday of one of our long time members, Joan Mercer. We had a special morning tea after our Calligraphy class complete with birthday cake and a Birthday Tiara for Joan.”<br>Happy birthday Joan</div>
  </article>

  <article class="district-card logan">
    <div class="label">Logan: from Helen Carver</div>
    <div class="photo"><div role="img" aria-label="Portrait photo of the departing Spanish tutor"></div></div>
    <div class="quote">“Logan District students are sad that we will soon lose Dorothy Lane who has taught Spanish in her inimitable style to hundreds of students in the city and in Logan. Dot is moving to Victoria Point at the end of May and plans to teach Spanish for Redlands ALP. Our loss is their gain and we hope Dot will be very happy in her new home. Meanwhile students are hoping to find another Spanish tutor for Logan. Any offers?”</div>
  </article>

  <div class="footer-bands"><div class="a"></div><div class="b"></div><div class="c"></div></div>
</body>
</html>
```